Pamphlet for IT Services Company (MSP Provider or Managed Services Provider)

We need a pamphlet designed for our Managed Services Company. We are an established company of 17 years that has never advertised. We'd like a pamphlet that we can drop off at potential client sites that describes our services. I like clean and prefer Orange as an accent color. We'd like to touch on the fact that we cater to our clients needs and go above and beyond what the other providers do.

Target Market(s)

Small and Medium Sized Businesses

Industry/Entity Type

It Service

Font styles to use
Other font styles liked:
• Try to match font on logo or website

Requirements
Must have
• Must highlight with the following Services and descriptions with Logo
Managed IT Services
IT Support
VOIP Solutions
WiFI Solutions
Contact information with phone number and website address.
Please view website korvantech.com
try to match fons on website above.
Nice to have
• Customer Testimonials. May a couple one line testimonials. Not real sure because this is the first time we've ever designed a brochure.
Should not have
• Not Sure

```html
<!DOCTYPE html>
<html lang="en">
<head>
<meta charset="utf-8">
<title>Korvan Tech – Managed IT Services</title>
<link rel="stylesheet" href="https://fonts.googleapis.com/css2?family=Montserrat:wght@400;500;600;700;800;900&family=Oswald:wght@500;600&display=swap">
<style>
:root{
  --orange:#f47b20;
  --orange-dark:#d9620d;
  --navy:#1e2531;
  --navy-2:#2a3342;
  --slate:#5e6879;
  --slate-light:#8b94a3;
  --text:#3a3f47;
  --white:#ffffff;
  --page:#e6e7ea;
}
*{box-sizing:border-box;margin:0;padding:0}
html,body{width:1200px;height:613px;overflow:hidden;background:var(--page)}
body{font-family:"Montserrat",sans-serif;color:var(--text)}
.flyer{position:absolute;left:395px;top:16px;width:410px;height:580px;background:var(--white);overflow:hidden;box-shadow:0 4px 14px rgba(0,0,0,.25)}
.abs{position:absolute}

.header{left:0;top:0;width:410px;height:58px;background:linear-gradient(#fff,#f3f3f4)}
.brand{left:19px;top:18px;display:flex;align-items:center;gap:8px;font-family:"Montserrat",sans-serif;font-weight:700;font-size:18px;color:var(--navy);letter-spacing:.5px}
.brand-dot{width:14px;height:14px;border-radius:50%;background:var(--orange)}

.hero{left:0;top:58px;width:410px;height:118px;background:var(--navy)}
.hero-photo{left:165px;top:58px;width:245px;height:155px;background:linear-gradient(90deg,var(--navy) 0%,rgba(30,37,49,.6) 18%,rgba(60,70,85,.3) 45%,rgba(120,80,55,.55) 80%,rgba(140,90,60,.7) 100%),linear-gradient(180deg,#3a4556 0%,#55697a 45%,#2b3340 100%)}
.hero-title{left:19px;top:62px;font-weight:900;font-size:26px;line-height:24px;color:var(--white);letter-spacing:.2px}
.hero-title .accent{color:var(--orange)}
.hero-sub{left:19px;top:114px;font-weight:500;font-size:10.5px;line-height:12.5px;color:var(--white)}

.tagline{left:0;top:163px;width:250px;height:50px;background:var(--orange);clip-path:polygon(0 0,205px 0,250px 100%,0 100%)}
.tagline-mark{left:14px;top:158px;font-weight:900;font-size:42px;color:var(--orange-dark);line-height:1}
.tagline-text{left:15px;top:177px;font-weight:800;font-size:11.5px;line-height:12.5px;color:var(--white)}

.service{width:165px;height:80px;background:linear-gradient(135deg,#fafafa,#ececee);border-radius:10px;box-shadow:0 2px 5px rgba(0,0,0,.14)}
.service-icon{width:46px;height:46px;border-radius:50%;border:3px solid #fff;box-shadow:0 2px 5px rgba(0,0,0,.25);display:flex;align-items:center;justify-content:center}
.icon-slate{background:var(--slate)}
.icon-light{background:#f2f1ee}
.icon-orange{background:var(--orange)}
.icon-navy{background:var(--navy)}
.service-body{width:125px}
.service-title{font-weight:800;font-size:9px;letter-spacing:.2px;color:var(--navy)}
.service-title.orange{color:var(--orange)}
.service-title.slate{color:var(--slate)}
.service-lead{font-weight:700;font-size:7px;color:var(--navy);margin:2px 0 3px}
.service-text{font-size:5.6px;line-height:7.4px;text-align:justify;color:var(--text);margin-top:3px}

.testimonial{left:0;top:403px;width:410px;height:72px;background:var(--slate);clip-path:polygon(0 0,14px 9px,100% 9px,100% 100%,0 100%)}
.quote-open,.quote-close{font-weight:900;font-size:64px;line-height:1;color:var(--slate-light)}
.quote-open{left:14px;top:418px}
.quote-close{left:350px;top:404px}
.testimonial-text{left:81px;top:421px;width:250px;font-size:5.7px;line-height:8px;color:var(--white)}
.testimonial-author{left:81px;top:458px;width:250px;text-align:right;font-weight:700;font-size:5.7px;color:var(--white)}

.partners{left:12px;top:480px;width:386px;height:30px;display:flex;align-items:center;justify-content:space-between}
.partner{background:#d7d9de;border-radius:3px;height:24px}
.partner.dark{background:#3b4250}

.footer-line{left:0;top:511px;width:410px;height:4px;background:var(--orange)}
.footer{left:0;top:515px;width:410px;height:65px;background:var(--navy)}
.follow{right:16px;top:518px;font-weight:600;font-size:7.5px;color:var(--white)}
.help{left:0;top:540px;width:78px;height:31px;background:var(--orange);clip-path:polygon(0 0,100% 0,86% 100%,0 100%);padding:2px 0 0 8px;color:var(--white);font-weight:800;line-height:8.5px}
.help small{display:block;font-size:6.5px;font-weight:600}
.help span{display:block;font-size:8.5px}
.phone-icon{left:84px;top:540px}
.phone{left:113px;top:533px;font-family:"Oswald",sans-serif;font-weight:600;font-size:20px;color:var(--white);letter-spacing:.5px}
.address{left:113px;top:561px;font-size:7.3px;color:var(--white);letter-spacing:.2px}
.divider{left:296px;top:543px;width:1px;height:27px;background:#59606c}
.contact{left:302px;top:544px;font-weight:700;font-size:6.8px;line-height:10.5px;color:var(--white)}
.contact i{display:inline-block;width:5px;height:5px;border:1px solid var(--orange);margin-right:4px;vertical-align:middle}
</style>
</head>
<body>
<main class="flyer">
  <div class="abs header"></div>
  <div class="abs brand"><span class="brand-dot"></span>Korvan Tech</div>

  <div class="abs hero"></div>
  <div class="abs hero-photo" role="img" aria-label="Laptop on a desk showing an analytics dashboard"></div>
  <h1 class="abs hero-title"><span class="accent">MANAGED</span><br>IT SERVICES</h1>
  <p class="abs hero-sub">A SIMPLE, COST EFFECTIVE<br>PLAN FOR YOUR IT<br>INFRASTRUCTURE.</p>

  <div class="abs tagline"></div>
  <div class="abs tagline-mark">“</div>
  <p class="abs tagline-text">WOULDN'T IT BE NICE IF<br>YOUR STUFF JUST WORKED?</p>

  <section class="abs service" style="left:37px;top:237px"></section>
  <div class="abs service-icon icon-slate" style="left:16px;top:254px">
    <svg width="20" height="22" viewBox="0 0 20 22"><path d="M10 1 L18 4 V10 C18 15 14 19 10 21 C6 19 2 15 2 10 V4 Z" fill="#fff"/><path d="M7 6 H13 V11 C13 13 11.5 14.5 10 15.5 C8.5 14.5 7 13 7 11 Z" fill="#5e6879"/></svg>
  </div>
  <div class="abs service-body" style="left:70px;top:245px">
    <h2 class="service-title slate">MANAGED IT SERVICES</h2>
    <p class="service-lead">Let us take care of your IT</p>
    <p class="service-text">Our MSP is a Flat Rate service that includes Onsite &amp; Remote Support, Endpoint Protection, Web Filtering, Encrypted Online Backup &amp; Patch Management</p>
  </div>

  <section class="abs service" style="left:228px;top:237px"></section>
  <div class="abs service-icon icon-light" style="left:207px;top:254px">
    <svg width="22" height="24" viewBox="0 0 22 24" fill="none" stroke="#2a3342" stroke-width="2"><circle cx="11" cy="7" r="5"/><path d="M2 22 V19 C2 15 5 13 9 13 H13 C17 13 20 15 20 19 V22 Z"/></svg>
  </div>
  <div class="abs service-body" style="left:260px;top:250px">
    <h2 class="service-title">IT SUPPORT</h2>
    <p class="service-text">We have a passion for what we do and it shows! Korvan provides fast, reliable, expert solutions from experienced staff. You will never feel like just another client to us because our customers are family!</p>
  </div>

  <section class="abs service" style="left:37px;top:327px"></section>
  <div class="abs service-icon icon-orange" style="left:16px;top:344px">
    <svg width="24" height="24" viewBox="0 0 24 24" fill="none" stroke="#fff" stroke-width="2" stroke-linecap="round"><path d="M8 4 L5 5 C3 9 5 16 10 20 L13 19 L12 15 L10 15 C8.5 13 8 11 8 9 L10 8 Z" fill="#fff"/><path d="M14 8 A4 4 0 0 1 14 13"/><path d="M17 6 A7 7 0 0 1 17 15"/><path d="M20 4 A10 10 0 0 1 20 17"/></svg>
  </div>
  <div class="abs service-body" style="left:70px;top:331px">
    <h2 class="service-title orange">VOIP SOLUTIONS</h2>
    <p class="service-text">Phones are more than just an attachment to a desk. Allow us to help you maximize communication with your team and customers by using the latest technology that will likely save you money as well. Korvan Technologies partners with Calloway Voice to provide phone hardware, systems, and phone service</p>
  </div>

  <section class="abs service" style="left:228px;top:327px"></section>
  <div class="abs service-icon icon-navy" style="left:207px;top:344px">
    <svg width="24" height="20" viewBox="0 0 24 20" fill="none" stroke="#fff" stroke-width="2.4" stroke-linecap="round"><path d="M2 7 A14 14 0 0 1 22 7"/><path d="M5.5 11 A9 9 0 0 1 18.5 11"/><path d="M9 14.5 A4 4 0 0 1 15 14.5"/><circle cx="12" cy="17.5" r="1.2" fill="#fff"/></svg>
  </div>
  <div class="abs service-body" style="left:260px;top:345px">
    <h2 class="service-title">WIFI SOLUTIONS</h2>
    <p class="service-text">WiFi is everywhere! (At least it should be.) Korvan can extend your WiFi to cover your whole campus</p>
  </div>

  <div class="abs testimonial"></div>
  <div class="abs quote-open">“</div>
  <div class="abs quote-close">”</div>
  <p class="abs testimonial-text">Lorem Ipsum is simply dummy text of the printing and typesetting industry. Lorem Ipsum has been the industry's standard dummy text ever since the 1500s, when an unknown printer took a galley of type and scrambled it to make a type specimen book.</p>
  <p class="abs testimonial-author">- Lorem Ipsum Dummy Text</p>

  <div class="abs partners" aria-label="Technology partners">
    <div class="partner" style="width:44px"></div>
    <div class="partner" style="width:38px"></div>
    <div class="partner" style="width:72px"></div>
    <div class="partner dark" style="width:98px"></div>
    <div class="partner" style="width:74px"></div>
  </div>

  <div class="abs footer-line"></div>
  <div class="abs footer"></div>
  <p class="abs follow">Follow Us on @korvantech</p>
  <div class="abs help"><small>How can we help?</small><span>CONTACT US</span><span>ANYTIME</span></div>
  <svg class="abs phone-icon" width="24" height="28" viewBox="0 0 24 28" fill="none" stroke="#f47b20" stroke-width="2" stroke-linecap="round"><rect x="6" y="2" width="13" height="24" rx="2"/><line x1="10" y1="22.5" x2="15" y2="22.5"/><path d="M4 9 C1 12 1 17 4 20"/><path d="M9 11 A4 4 0 0 1 9 17" stroke-width="1.6"/><path d="M12 9 A7 7 0 0 1 12 19" stroke-width="1.6"/></svg>
  <p class="abs phone">+1 (555) 014-2390</p>
  <p class="abs address">YOUR COMPANY ADDRESS GOES HERE</p>
  <div class="abs divider"></div>
  <p class="abs contact"><i></i>INFO@KORVANTECH.COM<br><i style="border-radius:50%"></i>WWW.KORVANTECH.COM</p>
</main>
</body>
</html>
```